Tech Website

1. Overview
Lumora9, formally named VantaSight, is a pioneer in computer vision technology and machine learning. Based out of Santa Clara, California, Lumora9 is at the forefront of the User Interface revolution; building technology architecture that grants devices with the aptitude to respond to emotional detection, gaze tracking, facial recognition, age and gender identification and gaming interaction. Winner of the Mobile Track at BRISK Founders Sprint 2012, Lumora9 has developed the next generation of consumer behaviour analytics. Lumora9 software solutions are scalable across various platforms including mobile phone, tablets, PC and SmartTV.
Updates

Good day, 

Please see the update to our brief - there is a PDF of the type of format and design we are looking for.  It shows each page - Landing, Technology, Product, Press and Company.

Thank you for your designs

Regards,

Target Market(s)

Target market - A mix of enterprise and consumer audiences, targeting the need for the technology in the living room space

Industry/Entity Type

Architecture

Requirements
Must have
• Design preferences - Easy to navigate, modern with sleek feel, trendy, tech saavy, using cube as a consistent element/theme. colours are not determined, but parrot green was one idea with 2 additional underlying colours. keys words like user interface revolution or sense recognition are good sources to draw inspiration.

Landing page will have a video - illustrating different uses of technology

Technical Specs - Landing page, 6 tabs/subpages, and each subpage may have 1 or 2 additional pages. Coding will be necessary, not that much at the beginning stages.

```html
<!DOCTYPE html>
<html lang="en">
<head>
<meta charset="utf-8">
<title>Lumora9 – Home</title>
<link href="https://fonts.googleapis.com/css2?family=PT+Sans:ital,wght@0,400;0,700;1,400&family=Lato:wght@300;400;700&family=Oswald:wght@500&display=swap" rel="stylesheet">
<style>
  :root{
    --lime:#c3dc16;
    --lime-deep:#8fba1c;
    --green-text:#7aa914;
    --ink:#1a1a1a;
    --body:#555;
    --header-top:#3a3a3a;
    --header-bottom:#0c0c0c;
    --btn-dark:#222;
    --date:#b3262a;
    --rule:#d6d6d6;
  }
  *{margin:0;padding:0;box-sizing:border-box}
  html,body{width:916px;height:1200px;overflow:hidden;background:#fff}
  body{position:relative;font-family:"Lato",sans-serif;color:var(--body)}
  .abs{position:absolute}

  /* header */
  .site-header{left:0;top:0;width:916px;height:96px;
    background:linear-gradient(#4a4a4a 0,#1e1e1e 40%,var(--header-bottom) 100%)}
  .logo{left:42px;top:28px;font-family:"PT Sans",sans-serif;font-size:36px;color:#fff;letter-spacing:.5px}
  .main-nav{right:0;top:44px;display:flex;align-items:center;height:33px}
  .main-nav a{font-family:"PT Sans",sans-serif;font-size:14px;color:var(--lime);text-decoration:none;padding:0 22px;border-left:1px solid #333;line-height:20px}
  .main-nav a.home{background:var(--lime);color:#1e2a00;border-radius:17px;padding:6px 21px;border:none;margin-right:8px}
  .main-nav a.first{border-left:none}
  .main-nav a:last-child{padding-right:50px}

  /* hero */
  .hero{left:0;top:96px;width:916px;height:361px;
    background:radial-gradient(ellipse at 45% 20%,#cde320 0,var(--lime) 35%,#8fbe21 100%)}
  .hero h1{left:49px;top:58px;font-family:"PT Sans",sans-serif;font-weight:400;font-size:31px;color:#2e3a0c;white-space:nowrap}
  .hero h2{left:49px;top:99px;font-family:"PT Sans",sans-serif;font-weight:400;font-size:23px;color:#3d4a12}
  .hero p{left:49px;top:138px;width:325px;font-family:"PT Sans",sans-serif;font-style:italic;font-size:11px;line-height:17px;color:#fff}
  .btn-dark{top:217px;height:31px;background:var(--btn-dark);color:#fff;font-family:"Oswald",sans-serif;font-size:12.5px;letter-spacing:.3px;display:flex;align-items:center;justify-content:center;gap:7px;border-radius:2px}
  .btn-dark svg{width:5px;height:8px}
  .hero-visual{left:479px;top:22px;width:370px;height:302px;border-radius:22px;
    background:linear-gradient(135deg,#6e6e6e,#1f1f1f 30%,#4b8a2c 55%,#7cb84a 80%,#2a2a2a)}
  .slider-dots{left:430px;top:343px;display:flex;gap:4px}
  .slider-dots span{width:9px;height:9px;border-radius:50%;background:#f2f6d8;opacity:.9}

  /* intro */
  .welcome h3,.uses h3{font-family:"PT Sans",sans-serif;font-weight:400;font-size:18px;color:var(--ink)}
  .welcome{left:32px;top:484px;width:525px}
  .welcome h3{margin-left:2px;margin-bottom:9px}
  .welcome p{font-size:10.6px;line-height:18.5px;text-align:justify;margin-bottom:8px;font-weight:300;color:#444}
  .welcome p b{font-weight:700}
  .welcome p.gap{margin-top:14px}
  .uses{left:588px;top:484px;width:298px}
  .video{left:588px;top:518px;width:298px;height:209px;
    background:linear-gradient(120deg,#e7e4d8 0,#bfb7a2 40%,#6e6a5c 75%,#3c3a33 100%)}
  .video-bar{left:588px;top:696px;width:298px;height:31px;background:#333}

  .divider{left:27px;top:761px;width:860px;height:1px;background:var(--rule)}

  /* product */
  .section-title{font-family:"PT Sans",sans-serif;font-weight:400;font-size:16.5px;color:var(--green-text)}
  .card-img{top:819px;width:228px;height:106px}
  .card h4{font-family:"Lato",sans-serif;font-weight:700;font-size:10.5px;color:#333;margin-bottom:8px}
  .card p{font-size:10.3px;line-height:16.8px;font-weight:300;color:#555}
  .btn-green{height:27px;width:87px;background:linear-gradient(#8ec63a,#5f9a1e);color:#fff;font-family:"PT Sans",sans-serif;font-size:11px;display:flex;align-items:center;justify-content:center;border-radius:2px}

  /* feed */
  .feed{left:586px;top:786px;width:305px}
  .feed .intro{font-size:10.6px;color:#555;margin-top:4px;margin-bottom:16px;font-weight:300}
  .tweet{margin-bottom:17px}
  .tweet h5{font-family:"Lato",sans-serif;font-weight:400;font-size:11.7px;color:#222;margin-bottom:6px}
  .tweet p{font-size:10.2px;line-height:15px;color:#444;font-weight:300}
  .tweet time{display:block;font-size:9.2px;color:var(--date);margin-top:4px}

  /* footer */
  .site-footer{left:0;top:1120px;width:916px;height:80px;border-top:1px solid #e6e6e6;box-shadow:inset 0 4px 5px -4px rgba(0,0,0,.12)}
  .footer-nav{left:35px;top:22px;display:flex;font-size:10.6px;color:#555;font-weight:300}
  .footer-nav a{color:inherit;text-decoration:none;padding:0 9px;border-left:1px solid #999;line-height:11px}
  .footer-nav a:first-child{padding-left:0;border-left:none}
  .copyright{left:36px;top:48px;font-size:9.5px;color:#666;font-weight:300}
  .social{left:780px;top:17px;display:flex;gap:6px}
  .social span{width:19px;height:19px;border-radius:2px}
</style>
</head>
<body>

<header class="site-header abs">
  <div class="logo abs">Lumora9</div>
  <nav class="main-nav abs">
    <a class="home" href="#">Home</a>
    <a class="first" href="#">About Us</a>
    <a href="#">Press</a>
    <a href="#">Technology</a>
    <a href="#">Contact Us</a>
  </nav>
</header>

<section class="hero abs">
  <h1 class="abs">Allows Moble Applications to</h1>
  <h2 class="abs">Levarage Front Facing Camera</h2>
  <p class="abs">Ut ante enim, dapibus malesuada, fringilla eu, condimentum quis, tellus. Aenean porttitor eros vel dolor. Donec convallis pede venenatis nibh. Duis quam. Nam eget lacus. Aliquam erat volutpat. Quisque dignissim congue leo.</p>
  <a class="btn-dark abs" style="left:49px;width:101px">LEARN MORE <svg viewBox="0 0 5 8"><path d="M0 0L5 4L0 8Z" fill="#fff"/></svg></a>
  <a class="btn-dark abs" style="left:160px;width:100px">ORDER NOW <svg viewBox="0 0 5 8"><path d="M0 0L5 4L0 8Z" fill="#fff"/></svg></a>
  <div class="hero-visual abs" role="img" aria-label="Two smartphones showing a camera app framing a child sitting on grass"></div>
  <div class="slider-dots abs"><span></span><span></span><span></span><span></span></div>
</section>

<section class="welcome abs">
  <h3>Welcome to Lumora9 Website Mainpage</h3>
  <p><b>At VantaSight, we have been working on a architecture that is scalable</b>, parallelized and runs hierarchy of algorithms performing real-time and robust computation in the area of computer vision and machine learning.</p>
  <p>The scalability factor allows us to work across devices like mobile phone/tablet/PC/SmartTV. Some of the technology that we have touched are Emotion detection, Gaze Tracking, Gender Detection, Face Recognition, Gesture recognition, vision enabled Gaming etc. While writing our architecture, we have been very careful about how users interact with mobile devices. Our architecture and algorithms are pretty robust to change in lighting conditions, pose changes and jerky motions of the devices</p>
  <p class="gap">Mauris vel lacus vitae felis vestibulum volutpat. Etiam est nunc, venenatis in, tristique eu, imperdiet ac, nisl. Cum sociis natoque penatibus et magnis dis parturient montes, nascetur ridiculus mus. In iaculis facilisis massa. Etiam eu urna. Sed porta. Suspendisse quam leo, molestie sed, luctus quis, feugiat in, pede. Fusce tellus.</p>
</section>

<section class="uses abs"><h3>Uses of Technology</h3></section>
<div class="video abs" role="img" aria-label="Video still of a man filming with a compact camera"></div>
<div class="video-bar abs">
  <svg width="298" height="31" viewBox="0 0 298 31">
    <circle cx="20" cy="15.5" r="10" fill="none" stroke="#ccc" stroke-width="1.6"/>
    <path d="M17 10.5L25 15.5L17 20.5Z" fill="#ccc"/>
    <rect x="40" y="14" width="206" height="3" fill="#eee"/>
    <path d="M262 12h4l5-4v15l-5-4h-4z" fill="none" stroke="#aaa" stroke-width="1.2"/>
    <path d="M274 11q3 4.5 0 9M277 9q5 6.5 0 13" fill="none" stroke="#aaa" stroke-width="1.2"/>
  </svg>
</div>

<div class="divider abs"></div>

<h3 class="section-title abs" style="left:36px;top:786px">Why Choose Our Product?</h3>

<div class="card-img abs" style="left:34px;background:linear-gradient(120deg,#3d7fd6,#1b2a4a 45%,#0c0c0c 65%,#6fa7e6)" role="img" aria-label="Tablet lying on a field of app icons"></div>
<div class="card-img abs" style="left:301px;background:linear-gradient(100deg,#1a1a1a,#2f5d4a 35%,#d9c7a8 55%,#3a3a3a 80%,#111)" role="img" aria-label="Person holding a tablet during a video call"></div>

<div class="card abs" style="left:35px;top:940px;width:245px">
  <h4>Who is this for?</h4>
  <p>This program is for pref cooks, dishwashers, bussers, runners, servers, hosts/hostesses and anyone else who handles food but is not primarily responsible for its safety. The course will train on proper food handling principles.</p>
</div>
<div class="card abs" style="left:306px;top:940px;width:245px">
  <h4>How it works</h4>
  <p>This program is for pref cooks, dishwashers, bussers, runners, servers, hosts/hostesses and anyone else who handles food but is not primarily responsible for its safety. The course will train on proper food handling principles.</p>
</div>
<a class="btn-green abs" style="left:32px;top:1059px">LEARN MORE</a>
<a class="btn-green abs" style="left:306px;top:1055px">LEARN MORE</a>

<section class="feed abs">
  <h3 class="section-title">Latest News Murmur Feed</h3>
  <p class="intro">Learn, share, connect. Check out the latest tips, tricks</p>
  <article class="tweet">
    <h5>Pellentesque nibh libero</h5>
    <p>Ultricies eu, sagittis non, mollis sed, justo. Praesent metus ipsum, pulvinar pulvinar, porta id, fringilla at, est.</p>
    <time>Posted on 08 Nov 2012</time>
  </article>
  <article class="tweet">
    <h5>Lorem ipsum dolor sit amet, consectetuer adipiscing elit.</h5>
    <p>Ultricies eu, sagittis non, mollis sed, justo. Praesent metus ipsum, pulvinar pulvinar, porta id, fringilla at, est.</p>
    <time>Posted on 05 Nov 2012</time>
  </article>
  <article class="tweet" style="padding-left:3px">
    <h5>Donec scelerisque leo ac risus</h5>
    <p>Ultricies eu, sagittis non, mollis sed, justo. Praesent metus ipsum, pulvinar pulvinar, porta id, fringilla at, est.</p>
    <time>Posted on 01 Nov 2012</time>
  </article>
</section>

<footer class="site-footer abs">
  <nav class="footer-nav abs">
    <a href="#">Home</a><a href="#">About Us</a><a href="#">Press</a><a href="#">Technology</a><a href="#">Contact Us</a>
  </nav>
  <p class="copyright abs">Copyright 2012 VantaSight.&nbsp; All Rights Reserved</p>
  <div class="social abs" aria-label="Social links">
    <span style="background:#3b5b99"></span>
    <span style="background:#1c7cb5"></span>
    <span style="background:#e8741c"></span>
    <span style="background:#c4302b"></span>
  </div>
</footer>

</body>
</html>
```